I need some Graphic Design/UX/UI for a mobile app

I am looking for someone to provide complete UI/UX designs for a mobile app. These designs will form the basis for future development work so need to be suitable for handing over to developers. They also need to be of high enough quality to enable me to validate the ideas with potential users and sponsors of the app. I will also require a logo design to be incorporated. The name of the app is Trellin. The persistent theme needs to be cycling and road safety.

I can provide low fidelity wireframes:
[see file upload]
Which should hopefully help with the flow of the user journey through the app screens. But I am open to the designer suggesting additional design elements based on their experiences.

As well as Pinterest boards:
Which help illustrate the kind of theme I require.

I can also provide business requirements which help illustrate the user stories.
[file upload to follow]

By way of outputs I require something akin to an Adobe XD prototype of the app that I can use for demonstration purposes. It doesn't have to be Adobe XD however, so whatever you are most comfortable with.

```html
<!DOCTYPE html>
<html lang="en">
<head>
<meta charset="utf-8">
<title>Trellin Cycling – 2 Screens</title>
<link rel="stylesheet" href="https://fonts.googleapis.com/css2?family=Raleway:wght@300;400&family=Roboto:wght@300;400;500;700&display=swap">
<style>
  :root{
    --band:#3a3e66;
    --teal:#36c4c1;
    --sea:#2a8ec0;
    --sea-low:#2b8cbe;
    --white:#ffffff;
    --night:#1d2446;
    --night-deep:#141a35;
    --field:rgba(60,66,110,.55);
    --field-line:rgba(150,160,200,.45);
    --muted:#c8cce0;
    --icon-fill:#3a4270;
  }
  *{box-sizing:border-box;margin:0;padding:0}
  html,body{width:752px;height:1200px;overflow:hidden}
  body{position:relative;background:var(--sea);font-family:"Roboto",sans-serif;color:var(--white)}

  .title-band{position:absolute;left:0;top:0;width:752px;height:149px;background:var(--band);text-align:center}
  .title-band h1{font-family:"Raleway",sans-serif;font-weight:300;font-size:66px;line-height:1;padding-top:18px;letter-spacing:1px}
  .title-band p{font-family:"Raleway",sans-serif;font-weight:400;font-size:36px;color:var(--teal);margin-top:6px}

  .section-one{position:absolute;left:0;top:149px;width:752px;height:559px;background:var(--sea)}
  .section-two{position:absolute;left:0;top:708px;width:752px;height:492px;background:var(--sea-low)}

  .screen-label{position:absolute;font-weight:300;font-size:50px;white-space:nowrap;line-height:1}
  .screen-label strong{font-weight:700;font-size:66px;margin-left:8px}
  .label-one{left:443px;top:262px}
  .label-two{left:72px;top:724px}

  /* Login screen */
  .login-screen{position:absolute;left:73px;top:269px;width:195px;height:345px;overflow:hidden;background:var(--night-deep)}
  .login-backdrop{position:absolute;inset:0;background:linear-gradient(180deg,#2c3a63 0%,#3a4466 35%,#2a3050 60%,#161b38 100%)}
  .brand-disc{position:absolute;left:55px;top:58px;width:86px;height:86px;border-radius:50%;background:var(--white);display:flex;align-items:center;justify-content:center}
  .brand-disc span{font-family:"Roboto",sans-serif;font-weight:500;font-size:18px;color:var(--band)}

  .field{position:absolute;display:flex;align-items:center;border:1px solid var(--field-line);background:var(--field);border-radius:999px;color:var(--muted)}
  .field svg{flex:none}
  .field .divider{width:1px;background:var(--field-line);align-self:stretch}
  .login-screen .field{left:13px;width:171px;height:28px;font-size:10px;padding-left:11px}
  .login-screen .field svg{width:10px;height:10px;margin-right:6px}
  .login-screen .field .divider{margin:6px 6px 6px 0}
  .btn-start{position:absolute;background:var(--teal);color:var(--white);border-radius:999px;display:flex;align-items:center;justify-content:center;font-weight:500}
  .login-screen .btn-start{left:13px;top:268px;width:171px;height:30px;font-size:11px}
  .links{position:absolute;display:flex;justify-content:space-between;color:var(--muted)}
  .login-screen .links{left:13px;top:313px;width:171px;font-size:10px}

  /* Zoomed login detail */
  .login-detail{position:absolute;left:333px;top:368px;width:330px;height:258px;overflow:hidden;background:var(--night-deep)}
  .login-detail .login-backdrop{background:linear-gradient(180deg,#3a4466 0%,#2a3050 45%,#161b38 100%)}
  .login-detail .field{left:22px;width:290px;height:42px;font-size:16px;padding-left:20px}
  .login-detail .field svg{width:17px;height:17px;margin-right:10px}
  .login-detail .field .divider{margin:9px 10px 9px 0}
  .login-detail .btn-start{left:22px;top:151px;width:290px;height:42px;font-size:16px}
  .login-detail .links{left:22px;top:214px;width:290px;font-size:15px}

  /* Mode choice screen */
  .mode-screen{position:absolute;left:376px;top:760px;width:220px;height:400px;border-radius:6px;background:radial-gradient(circle at 50% 45%,#2b3360 0%,var(--night) 60%,var(--night-deep) 100%)}
  .mode-option{position:absolute;left:50px;width:120px;height:120px;border-radius:50%;background:var(--white);border:4px solid #5a6290;display:flex;align-items:center;justify-content:center}
  .mode-option .glyph{width:70px;height:56px;border-radius:10px;background:var(--icon-fill)}
  .mode-bike{top:70px}
  .mode-car{top:220px}
</style>
</head>
<body>

<header class="title-band">
  <h1>Trellin Cycling</h1>
  <p>2 Screens</p>
</header>

<section class="section-one"></section>
<section class="section-two"></section>

<div class="screen-label label-one">Screen<strong>01</strong></div>

<div class="login-screen">
  <div class="login-backdrop" role="img" aria-label="Dusk photo of a cyclist on a coastal road"></div>
  <div class="brand-disc"><span>Trellin</span></div>
  <div class="field" style="top:192px">
    <svg viewBox="0 0 16 16" fill="none" stroke="currentColor" stroke-width="1.4"><circle cx="8" cy="5" r="3"/><path d="M2 15c0-3.5 2.7-5.5 6-5.5s6 2 6 5.5z"/></svg>
    <span class="divider"></span>Username
  </div>
  <div class="field" style="top:230px">
    <svg viewBox="0 0 16 16" fill="none" stroke="currentColor" stroke-width="1.4"><rect x="2.5" y="7" width="11" height="8" rx="1"/><path d="M5 7V5a3 3 0 0 1 6 0v2"/></svg>
    <span class="divider"></span>Password
  </div>
  <div class="btn-start">Get Started</div>
  <div class="links"><span>New User</span><span>Need Help?</span></div>
</div>

<div class="login-detail">
  <div class="login-backdrop" role="img" aria-label="Dusk photo of a coastal road"></div>
  <div class="field" style="top:39px">
    <svg viewBox="0 0 16 16" fill="none" stroke="currentColor" stroke-width="1.2"><circle cx="8" cy="5" r="3"/><path d="M2 15c0-3.5 2.7-5.5 6-5.5s6 2 6 5.5z"/></svg>
    <span class="divider"></span>Username
  </div>
  <div class="field" style="top:95px">
    <svg viewBox="0 0 16 16" fill="none" stroke="currentColor" stroke-width="1.2"><rect x="2.5" y="7" width="11" height="8" rx="1"/><path d="M5 7V5a3 3 0 0 1 6 0v2"/></svg>
    <span class="divider"></span>Password
  </div>
  <div class="btn-start">Get Started</div>
  <div class="links"><span>New User</span><span>Need Help?</span></div>
</div>

<div class="screen-label label-two">Screen<strong>02</strong></div>

<div class="mode-screen">
  <div class="mode-option mode-bike"><div class="glyph" role="img" aria-label="Cyclist riding a bike icon"></div></div>
  <div class="mode-option mode-car"><div class="glyph" role="img" aria-label="Car front view icon"></div></div>
</div>

</body>
</html>
```